Roll up/retractable banner for trade show - higher education software company

My company, BrightOak Scholastics, will be attending a trade show soon, and we need a design for a "roll up" or "retractable" banner. According to the printer, it must be exactly 33 inches wide by 81 inches tall, at a DPI of 150 (not 300).

This is the exact product from Zubrix: https://zbrx.example/7Kq2LmN

The banner should have a professional feel and have a similar aesthetic to our brochure, web site, etc. Please see attached files. Use as much or as little as you see fit from the attached files. If you use stock photos in your design, just let me know where I need to go to purchase them.

Our software company focuses on advising and student success for colleges and universities. I like the idea of focusing on the "use cases" of our software, rather than specific software offerings, but I am open to interpretations.

Website: https://brightoakscholastics.example

REQUIREMENT
The final product MUST be in a file format which I can edit later on, with elements in different layers. Either Photoshop or GIMP will be fine, though I can also load .ai files. GIMP is actually preferred, but not required. Mainly, I must be able to alter text, move graphics around, swap out graphics, etc, as needed in the future. If you only work with psd and ai, please provide both file versions in the end.

Target Market(s)

University staff / VP's / presidents / decision-makers at trade shows and conferences

Industry/Entity Type

Higher Education / Software Development

Font styles to use
Sans Serif
Other font styles liked:
• MONTSERRAT is the font used in my logo and brochure, I use RALEWAY on the website. But these are not requirements-- Use what you think looks best.

Requirements
Must have
• 33"wide by 81" tall, 150 DPI. Professional appearance. Final files must be PSD, AI, or GIMP format so I can edit/tweak text and images later if needed. If using AI, please provide both .ai and .psd files.
Nice to have
• Similar wording/content/graphics/colors & fonts as brochure and website (see attached files). Especially some of the use-case wording from the brochure. Flashy and important information should be at the top of the banner, because if this is placed behind a table in a booth, info on the bottom might be obscured or hidden. The QR code from the brochure might be nice to have as well.

```html
<!DOCTYPE html>
<html lang="en">
<head>
<meta charset="utf-8">
<title>BrightOak Scholastics – Roll-up Banner</title>
<link rel="stylesheet" href="https://fonts.googleapis.com/css2?family=Montserrat:wght@400;600;700;800&family=Open+Sans:wght@400;600;700&display=swap">
<style>
  :root {
    --stage: #6b6b6b;
    --paper: #f4f4f4;
    --pink: #d63a7c;
    --orange: #e6892a;
    --blue: #2a8ac4;
    --ink: #1e1e1e;
    --text: #2f2f2f;
    --footer: #2d2d2d;
    --footer-text: #ececec;
    --photo-a: #7b6450;
    --photo-b: #4f6e8f;
    --photo-c: #a89a8c;
  }
  * { box-sizing: border-box; margin: 0; padding: 0; }
  html, body { width: 1200px; height: 800px; overflow: hidden; }
  body { background: var(--stage); font-family: "Open Sans", Arial, sans-serif; }

  .banner {
    position: absolute; left: 445px; top: 20px;
    width: 310px; height: 760px;
    background: var(--paper);
    overflow: hidden;
  }
  .banner__hero { position: absolute; left: 0; top: 0; width: 310px; height: 405px; display: block; }

  .brand {
    position: absolute; left: 0; top: 34px; width: 310px;
    display: flex; align-items: center; justify-content: center; gap: 9px;
  }
  .brand__mark { width: 26px; height: 26px; border-radius: 50%; background: var(--orange); }
  .brand__name {
    font-family: "Montserrat", Arial, sans-serif; font-weight: 700;
    font-size: 19px; color: var(--ink); letter-spacing: 0.2px;
  }

  .pitch { position: absolute; left: 0; top: 414px; width: 310px; text-align: center; }
  .pitch__headline {
    font-family: "Montserrat", Arial, sans-serif; font-weight: 800;
    font-size: 17.5px; line-height: 23px; letter-spacing: 0.1px;
  }
  .pitch__headline .c-pink { color: var(--pink); display: block; }
  .pitch__headline .c-orange { color: var(--orange); display: block; }
  .pitch__headline .c-blue { color: var(--blue); display: block; }
  .pitch__tagline {
    margin-top: 6px;
    font-family: "Montserrat", Arial, sans-serif; font-weight: 600;
    font-size: 13.5px; line-height: 18px; color: var(--ink);
  }

  .facts { position: absolute; left: 16px; top: 532px; width: 282px; }
  .facts__title {
    font-family: "Montserrat", Arial, sans-serif; font-weight: 800; font-size: 12px;
    margin-bottom: 6px;
  }
  .facts__title .c-pink { color: var(--pink); }
  .facts__title .c-orange { color: var(--orange); }
  .facts__title .c-blue { color: var(--blue); }
  .fact { display: flex; align-items: center; gap: 10px; margin-bottom: 9px; }
  .fact__icon { flex: 0 0 32px; width: 32px; height: 32px; }
  .fact__name { font-weight: 700; font-size: 11px; color: var(--ink); line-height: 13px; }
  .fact__text { font-size: 9.6px; line-height: 12.5px; color: var(--text); }

  .contact {
    position: absolute; left: 0; bottom: 0; width: 310px; height: 76px;
    background: var(--footer); color: var(--footer-text);
    font-family: "Montserrat", Arial, sans-serif; font-size: 12px; line-height: 17px;
    text-align: center; padding-top: 13px; font-weight: 400;
  }
  .contact__phone { font-weight: 600; color: #fff; }
</style>
</head>
<body>
<main class="banner">
  <svg class="banner__hero" viewBox="0 0 310 405" aria-hidden="false">
    <defs>
      <linearGradient id="photoTone" x1="0" y1="0" x2="1" y2="1">
        <stop offset="0" stop-color="var(--photo-a)"/>
        <stop offset="0.55" stop-color="var(--photo-c)"/>
        <stop offset="1" stop-color="var(--photo-b)"/>
      </linearGradient>
    </defs>
    <polygon role="img" aria-label="Photo: university advisors reviewing student data together at a computer in an office" points="0,128 310,104 310,405 0,405" fill="url(#photoTone)"/>
    <polygon points="0,405 310,290 310,405" fill="var(--pink)"/>
    <polygon points="30,405 310,322 310,405" fill="var(--orange)" stroke="#fff" stroke-width="2"/>
    <polygon points="120,405 310,362 310,405" fill="var(--blue)" stroke="#fff" stroke-width="2"/>
  </svg>

  <header class="brand">
    <span class="brand__mark"></span>
    <span class="brand__name">BrightOak Scholastics</span>
  </header>

  <section class="pitch">
    <h1 class="pitch__headline">
      <span class="c-pink">ACADEMIC ADVISING EARLY</span>
      <span class="c-orange">ALERTS TEXT MESSAGING</span>
      <span class="c-blue">APPOINTMENTS &amp; MORE</span>
    </h1>
    <p class="pitch__tagline">Student Success has never been<br>so intuitive and powerful</p>
  </section>

  <section class="facts">
    <h2 class="facts__title"><span class="c-pink">FACTS</span> <span class="c-orange">ABOUT</span> <span class="c-blue">SERVICE:</span></h2>

    <div class="fact">
      <svg class="fact__icon" viewBox="0 0 32 32" aria-hidden="true">
        <circle cx="16" cy="16" r="14.5" fill="#fff" stroke="var(--orange)" stroke-width="2"/>
        <path d="M11 21 L21 11 M15 11 H21 V17" fill="none" stroke="var(--pink)" stroke-width="2.2" stroke-linecap="round" stroke-linejoin="round"/>
      </svg>
      <div>
        <p class="fact__name">POWERFUL</p>
        <p class="fact__text">Gain the full picture with early alerts, predictive analytics, and advanced advising</p>
      </div>
    </div>

    <div class="fact">
      <svg class="fact__icon" viewBox="0 0 32 32" aria-hidden="true">
        <circle cx="16" cy="16" r="14.5" fill="#fff" stroke="var(--orange)" stroke-width="2"/>
        <circle cx="16" cy="16" r="6" fill="none" stroke="var(--pink)" stroke-width="3" stroke-dasharray="3 2"/>
        <circle cx="16" cy="16" r="2.2" fill="var(--blue)"/>
      </svg>
      <div>
        <p class="fact__name">FLEXIBLE</p>
        <p class="fact__text">BrightOak easily adapts to your university, not the other way around</p>
      </div>
    </div>

    <div class="fact">
      <svg class="fact__icon" viewBox="0 0 32 32" aria-hidden="true">
        <circle cx="16" cy="16" r="14.5" fill="#fff" stroke="var(--orange)" stroke-width="2"/>
        <circle cx="16" cy="16" r="8" fill="#1fa28c"/>
        <path d="M12.3 16.2 L15 18.8 L19.8 13.6" fill="none" stroke="#fff" stroke-width="2" stroke-linecap="round" stroke-linejoin="round"/>
      </svg>
      <div>
        <p class="fact__name">HASSLE-FREE</p>
        <p class="fact__text">Nothing to install on campus, and no need for additional IT team members</p>
      </div>
    </div>
  </section>

  <footer class="contact">
    <p>brightoakscholastics.example</p>
    <p class="contact__phone">555-014-2298</p>
    <p>info@brightoakscholastics.example</p>
  </footer>
</main>
</body>
</html>
```